Marlow Summit Holdings, LLC

I need a new business card desperately.

Please update my business card. I am looking for a professional modern classy design like the Brightfen Partners card in the attachments.

Industry/Entity Type

Investment

Contact Information for Business Card

Colors

Designer to choose colors to be used in the design.

```html
<!DOCTYPE html>
<html lang="en">
<head>
<meta charset="UTF-8">
<title>Marlow Summit Holdings — Business Card</title>
<link href="https://fonts.googleapis.com/css2?family=Lato:wght@400;700&display=swap" rel="stylesheet">
<style>
  :root {
    --navy: #11465f;
    --navy-deep: #0f3f56;
    --gold: #d4a75c;
    --paper: #ffffff;
    --stage: #26272b;
  }
  * { margin: 0; padding: 0; box-sizing: border-box; }
  html, body { width: 1200px; height: 800px; overflow: hidden; }
  body {
    background: var(--stage);
    font-family: "Lato", Arial, sans-serif;
    position: relative;
  }
  .card {
    position: absolute;
    width: 540px;
    height: 309px;
    top: 245px;
    overflow: hidden;
  }
  .card--front { left: 30px; background: var(--navy); }
  .card--back { left: 630px; background: var(--paper); }

  .brand {
    position: absolute;
    display: flex;
    align-items: center;
    gap: 12px;
    white-space: nowrap;
  }
  .brand__mark { width: 30px; height: 30px; flex: none; }
  .brand__name {
    font-weight: 700;
    font-size: 19px;
    line-height: 1.25;
    letter-spacing: 1.5px;
  }
  .card--front .brand { left: 50%; top: 50%; transform: translate(-50%, -50%); }
  .card--front .brand__mark { background: var(--gold); }
  .card--front .brand__name { color: var(--paper); }

  .card--back .brand { left: 200px; top: 98px; }
  .card--back .brand__mark { background: var(--navy); }
  .card--back .brand__name { color: var(--navy); font-size: 19px; }

  .web {
    position: absolute; top: 26px; right: 34px;
    font-size: 11px; color: var(--navy); font-weight: 700;
  }
  .web span { color: var(--gold); font-weight: 400; }

  .person { position: absolute; left: 30px; top: 108px; }
  .person__name { font-size: 15px; color: var(--navy); letter-spacing: .3px; }
  .person__name b { font-weight: 700; }
  .person__role { font-size: 13px; color: var(--gold); margin-top: 1px; }

  .divider {
    position: absolute; left: 40px; right: 60px; top: 218px;
    height: 1.5px; background: var(--gold);
  }
  .address {
    position: absolute; right: 36px; top: 176px;
    font-size: 12px; color: var(--navy); line-height: 1.4; text-align: right;
  }
  .contacts {
    position: absolute; left: 40px; top: 232px;
    font-size: 12.5px; color: var(--navy); line-height: 1.6;
  }
  .contacts__row { display: flex; align-items: center; gap: 7px; }
  .contacts__icon { width: 14px; height: 14px; flex: none; }
  .stripe {
    position: absolute; left: 0; right: 0; bottom: 0;
    height: 9px; background: var(--navy-deep);
  }
</style>
</head>
<body>
  <section class="card card--front">
    <div class="brand">
      <span class="brand__mark"></span>
      <span class="brand__name">MARLOW SUMMIT<br>HOLDINGS, LLC</span>
    </div>
  </section>

  <section class="card card--back">
    <p class="web">www.<span>MARLOWSUMMIT</span>.com</p>

    <div class="person">
      <p class="person__name"><b>NOLAN</b> REED</p>
      <p class="person__role">Owner</p>
    </div>

    <div class="brand">
      <span class="brand__mark"></span>
      <span class="brand__name">MARLOW SUMMIT<br>HOLDINGS, LLC</span>
    </div>

    <p class="address">PO BOX 418 Alder Rd,<br>7th Street, Ashford, USA</p>
    <div class="divider"></div>

    <div class="contacts">
      <div class="contacts__row">
        <svg class="contacts__icon" viewBox="0 0 14 14" aria-hidden="true">
          <circle cx="7" cy="7" r="7" fill="#d4a75c"/>
          <rect x="4.5" y="3.5" width="5" height="7" rx="1" fill="none" stroke="#fff" stroke-width="1.1"/>
        </svg>
        <span>(555) 014-2283</span>
      </div>
      <div class="contacts__row">
        <svg class="contacts__icon" viewBox="0 0 14 14" aria-hidden="true">
          <circle cx="7" cy="7" r="7" fill="#d4a75c"/>
          <rect x="3.5" y="4.5" width="7" height="5" fill="none" stroke="#fff" stroke-width="1"/>
          <path d="M3.5 4.5 L7 7.4 L10.5 4.5" fill="none" stroke="#fff" stroke-width="1"/>
        </svg>
        <span>hello@marlowsummit.com</span>
      </div>
    </div>

    <div class="stripe"></div>
  </section>
</body>
</html>
```